TOLO Electrical Services Letter Head

I need a professional clean looking design that will incorporate my company logo and information such as postal address, website, contact email "service@tolovoltworks.com.au" and phone number.

somewhere on the document i will also require my electrical contractor number "EC 046215" and my Australian Business number "57 139 604 282" these have to legally be on the document so they dont need to be a main feature, maybe in the footer in a smaller text.

Can you also have the 3 blue dashes from my logo as the watermark.

I would like the colour scheme to match my logo, business card and website www.tolovoltworks.com.au

I have the JPEG and PNG files for my logo which it will not allow me to upload as they are too wide, if you require these please let me know.

Target Market(s)

To be used for quotes and letters to commercial clients

Industry/Entity Type

Electric Company

Colors
0555a3
3176b5
85acd3
cfdfed
eaf1f7

Requirements
Must have
• company logo and information such as postal address, website, contact email "service@tolovoltworks.com.au" and phone number.
• somewhere on the document i will also require my electrical contractor number "EC 046215" and my Australian Business number "57 139 604 282" these have to legally be on the document so they dont need to be a main feature, maybe in the footer in a smaller text.
• I would like the colour scheme to match my logo, business card and website www.tolovoltworks.com.au
Nice to have
• Can you also have the 3 blue dashes from my logo as the watermark.

```html
<!DOCTYPE html>
<html lang="en">
<head>
<meta charset="utf-8">
<title>TOLO Electrical Services Letterhead</title>
<link href="https://fonts.googleapis.com/css2?family=Source+Sans+3:wght@400;700&display=swap" rel="stylesheet">
<style>
  :root {
    --ink: #151515;
    --text-grey: #555a60;
    --rule-grey: #c9ccd1;
    --paper-top: #ffffff;
    --paper-bottom: #f1f2f5;
    --band-light: #29a9e0;
    --band-dark: #1176bf;
    --footer-text: #ffffff;
  }
  * { margin: 0; padding: 0; box-sizing: border-box; }
  html, body { width: 933px; height: 1200px; overflow: hidden; }
  body { font-family: "Source Sans 3", "Helvetica Neue", Arial, sans-serif; background: #fff; }

  .letterhead {
    position: relative;
    width: 933px;
    height: 1200px;
    background: linear-gradient(160deg, var(--paper-top) 35%, var(--paper-bottom) 100%);
    overflow: hidden;
  }

  .brand {
    position: absolute;
    left: 31px;
    top: 44px;
    display: flex;
    align-items: center;
    gap: 12px;
  }
  .brand-square { width: 26px; height: 26px; background: var(--band-dark); }
  .brand-name {
    font-size: 34px;
    font-weight: 700;
    color: var(--ink);
    letter-spacing: 0.2px;
    white-space: nowrap;
  }

  .registration {
    position: absolute;
    left: 594px;
    top: 53px;
    padding-left: 16px;
    border-left: 1px solid var(--rule-grey);
    font-size: 16px;
    line-height: 24px;
    color: var(--text-grey);
    white-space: nowrap;
  }

  .footer-band {
    position: absolute;
    left: 0;
    bottom: 0;
    width: 933px;
    height: 155px;
  }
  .footer-wave { position: absolute; left: 0; top: 0; }

  .footer-contacts {
    position: absolute;
    left: 0;
    right: 0;
    bottom: 0;
    height: 155px;
    color: var(--footer-text);
    font-size: 16px;
  }
  .contact-row {
    position: absolute;
    left: 0;
    right: 0;
    display: flex;
    justify-content: center;
    align-items: center;
    gap: 16px;
    white-space: nowrap;
  }
  .contact-row.address { top: 99px; }
  .contact-row.lines { top: 127px; }
  .contact-item { display: flex; align-items: center; gap: 7px; line-height: 20px; }
  .contact-icon { display: block; flex: none; }
</style>
</head>
<body>
<main class="letterhead">
  <header>
    <div class="brand">
      <span class="brand-square"></span>
      <span class="brand-name">TOLO Electrical Services</span>
    </div>
    <div class="registration">
      <p>TOLO Electrical Services | EC 046215</p>
      <p>Australian Business Number : 57 139 604 282</p>
    </div>
  </header>

  <footer class="footer-band">
    <svg class="footer-wave" width="933" height="155" viewBox="0 0 933 155" aria-hidden="true">
      <path d="M0 0 Q466 138 933 0 L933 155 L0 155 Z" fill="var(--band-light)"/>
      <path d="M0 22 Q466 151 933 8 L933 155 L0 155 Z" fill="var(--band-dark)"/>
    </svg>
    <div class="footer-contacts">
      <div class="contact-row address">
        <span class="contact-item">
          <svg class="contact-icon" width="18" height="18" viewBox="0 0 18 18" aria-hidden="true">
            <circle cx="9" cy="9" r="9" fill="#fff"/>
            <path d="M9 3.5a3.6 3.6 0 0 0-3.6 3.6c0 2.7 3.6 6.6 3.6 6.6s3.6-3.9 3.6-6.6A3.6 3.6 0 0 0 9 3.5z" fill="var(--band-dark)"/>
            <circle cx="9" cy="7.1" r="1.4" fill="#fff"/>
          </svg>
          P.O Box 3318, Harbourside North, WA 6021
        </span>
      </div>
      <div class="contact-row lines">
        <span class="contact-item">
          <svg class="contact-icon" width="14" height="14" viewBox="0 0 14 14" aria-hidden="true">
            <circle cx="7" cy="7" r="6.2" fill="none" stroke="#fff" stroke-width="1.2"/>
            <path d="M5 3.6l1.3 1.6-.8 1c.5 1 1.2 1.7 2.2 2.2l1-.8 1.6 1.3-.9 1.2c-2.6-.4-4.6-2.4-5-5z" fill="#fff"/>
          </svg>
          (08) 6140 2259
        </span>
        <span class="contact-item">
          <svg class="contact-icon" width="16" height="14" viewBox="0 0 16 14" aria-hidden="true">
            <path d="M1 5.5 8 1l7 4.5V13H1z" fill="#fff"/>
            <path d="M1.5 6 8 10l6.5-4" fill="none" stroke="var(--band-dark)" stroke-width="1.2"/>
          </svg>
          service@tolovoltworks.com.au
        </span>
        <span class="contact-item">
          <svg class="contact-icon" width="14" height="14" viewBox="0 0 14 14" aria-hidden="true">
            <g fill="none" stroke="#fff" stroke-width="1.1">
              <circle cx="7" cy="7" r="6"/>
              <ellipse cx="7" cy="7" rx="2.6" ry="6"/>
              <path d="M1 7h12M2 4h10M2 10h10"/>
            </g>
          </svg>
          www.tolovoltworks.com.au
        </span>
      </div>
    </div>
  </footer>
</main>
</body>
</html>
```